Urgent * Legal Consultant Website Design

Provide a brief overview about your business Hello, website design required for independent legal consultant. Upload your company logo in the brief UPLOADED Specify the main navigation menu of your website (For better reference here's a sample of a website's navigation menu: (http://brovik88.net/wp-content/uploads/2012/css-menu/ 3.jpg) Header menu should include: About Us, Our people, Services and Contact Us Indicate the subpages or the dropdown menu if you have any (Refer to: http://pemtaz.co/wp-content/uploads/2010 /11/nav.jpg) No Subpages in the dropdown Upload to separate file for the text or the content needed for the homepage (This is a helpful supporting file to provide in order for our designers to better understand the elements needed on how to layout your This could be in Word document if you're using Windows or in Pages if you are using Mac. ) GET your legal advice and protect you and your BUSINESS Family Law Debt Recovery Leases Crimes & Traffic, wills Violence Restraining Orders Probate Titles Shariah Law Provide some samples of Web designs you like for better reference (Cite 2 to 3 samples) Website must be clean , simple and display our services in a clear way. Examples: https://cdn.vurdomix.com/wp/wp-content/uploads/sites/2/trosmo-simple-business-wordpress-theme-1024x846.jpg https://cdn.vurdomix.com/wp/wp -content / uploads / sites / 2 / pelinor-creative-studio-wp-website-template-1024x791.jpg Upload photos or files you would like to include in the design, or make mention if you are open to use stock photos Open to Use stock photos
Number of Pages Required
1 page
Look and feel
Each slider illustrates characteristics of the customer's brand and the style your logo design should communicate.

```html
<!DOCTYPE html>
<html lang="en">
<head>
<meta charset="utf-8">
<title>Lexmora Legal</title>
<link rel="stylesheet" href="https://fonts.googleapis.com/css2?family=Lato:ital,wght@0,400;0,700;0,900;1,400&display=swap">
<style>
:root{
  --yellow:#f6ea2b;
  --red:#e8303f;
  --ink:#1f1f1f;
  --body:#444;
  --muted:#7a7a7a;
  --white:#fff;
  --footer:#e6e6e6;
  --line:#d6d6d6;
}
*{margin:0;padding:0;box-sizing:border-box}
html,body{width:1200px;height:3066px;overflow:hidden}
body{font-family:'Lato',sans-serif;color:var(--ink);background:var(--white);position:relative}
.abs{position:absolute}
.btn{position:absolute;display:flex;align-items:center;justify-content:center;border-radius:22px;font-size:13px;font-weight:700;letter-spacing:.3px}
.btn-yellow{background:var(--yellow);color:var(--ink)}
.btn-red{background:var(--red);color:var(--white)}

/* header */
.site-header{top:0;left:0;width:1200px;height:94px;background:var(--white);border-bottom:1px solid var(--line)}
.brand{left:186px;top:30px;font-size:22px;font-weight:900;letter-spacing:.5px;color:var(--ink)}
.main-nav{left:433px;top:20px;width:581px;height:48px;background:var(--yellow);display:flex;align-items:center}
.main-nav a{font-size:14px;font-weight:700;color:var(--ink);text-decoration:none;height:48px;display:flex;align-items:center;padding:0 0 0 33px}
.main-nav a.active{background:var(--red);color:var(--white);padding:0 17px;margin-left:28px}
.dropdown{left:785px;top:68px;width:282px;height:304px;background:var(--red);padding:16px 0 0 34px;list-style:none;box-shadow:0 4px 10px rgba(0,0,0,.15);z-index:3}
.dropdown li{color:var(--white);font-size:13.5px;font-weight:700;height:35.6px;display:flex;align-items:center}

/* hero */
.hero{top:94px;left:0;width:1200px;height:505px;background:linear-gradient(90deg,#f4f4f2 0%,#ecebe8 35%,#c9bfb3 60%,#9b8f86 100%)}
.hero-title{left:192px;top:223px;font-size:35px;font-weight:900;line-height:37px}
.hero-title .red{color:var(--red)}
.hero-text{left:196px;top:350px;width:340px;font-size:14px;line-height:20px;color:var(--body)}
.slider-dots{display:flex;gap:6px}
.slider-dots span{width:11px;height:11px;border-radius:50%;background:#777}
.slider-dots span.ring{background:transparent;border:2px solid #777}

/* services */
.section-title{font-size:30px;font-weight:400;color:var(--ink)}
.services-title{left:0;width:1200px;top:652px;text-align:center}
.service{position:absolute;top:738px;width:200px}
.service svg{display:block}
.service h3{color:var(--red);font-size:19px;font-weight:900;margin-top:12px;line-height:20px}
.service p{font-size:13px;line-height:18px;color:var(--body);margin-top:8px}
.service .more{font-size:11px;font-weight:900;margin-top:6px}
.arrow{position:absolute;top:808px}

/* about */
.about-photo{left:0;top:1047px;width:599px;height:470px;background:linear-gradient(135deg,#cfd6de,#8e99a6 60%,#3c4048)}
.about-panel{left:599px;top:1047px;width:601px;height:470px;background:var(--yellow)}
.eyebrow{left:677px;top:1143px;font-size:16px;color:var(--ink)}
.about-title{left:675px;top:1166px;font-size:38px}
.about-text{left:677px;top:1220px;width:360px;font-size:14.5px;line-height:22px;color:var(--ink)}

/* testimonial */
.testimonial{left:0;top:1517px;width:1200px;height:409px;background:linear-gradient(90deg,#e9e9e9,#f3f3f3 50%,#dcdcdc)}
.client-title{left:450px;top:1590px;font-size:28px}
.avatar{left:194px;top:1656px;width:184px;height:184px;border-radius:50%;border:3px solid var(--red);background:linear-gradient(160deg,#c9a17f,#8a6a50)}
.quote-mark{left:349px;top:1729px}
.quote{left:447px;top:1668px;width:520px;font-size:17px;font-style:italic;line-height:33px;color:#333}
.author{left:450px;top:1780px;font-size:15px;font-weight:700;letter-spacing:.5px}

/* why */
.why-panel{left:0;top:1926px;width:599px;height:470px;background:var(--red)}
.why-photo{left:599px;top:1926px;width:601px;height:470px;background:linear-gradient(135deg,#d7d2cb,#a79d92 55%,#5e6774)}
.why-title{left:186px;top:2025px;font-size:34px;color:var(--white)}
.why-text{left:188px;top:2082px;width:360px;font-size:13.5px;line-height:25px;color:var(--white)}

/* people */
.people-title{left:186px;top:2456px;font-size:32px}
.people-text{left:186px;top:2508px;width:800px;font-size:16.5px;line-height:25.5px;color:var(--muted)}
.member{position:absolute;top:2623px;width:184px}
.member .photo{width:184px;height:178px;border:1px solid #999;background:linear-gradient(180deg,#e9e9e9,#c9c9c9 55%,#3d3f46)}
.member h4{color:var(--red);font-size:18px;font-weight:400;margin-top:16px;line-height:20px}
.member span{font-size:15px;color:var(--ink)}

/* footer */
.site-footer{left:0;top:2927px;width:1200px;height:139px;background:var(--footer)}
.footer-nav{left:191px;top:2966px;display:flex;gap:45px;font-size:13px;font-weight:700}
.copyright{left:191px;top:3002px;font-size:12.5px;color:#444}
.socials{left:867px;top:2962px;display:flex;gap:6px}
.socials span{width:33px;height:33px;border-radius:50%;background:var(--white);border:1px solid #ccc}
</style>
</head>
<body>

<header class="site-header abs">
  <div class="brand abs">LEXMORA LEGAL</div>
  <nav class="main-nav abs">
    <a>HOME</a><a>ABOUT US</a><a>OUR PEOPLE</a><a class="active">SERVICES</a><a>CONTACT US</a>
  </nav>
  <ul class="dropdown abs">
    <li>FAMILY LAW</li><li>DEBT RECOVERY</li><li>LEASES</li><li>CRIMES &amp; TRAFFIC, WILLS</li>
    <li>VIOLENCE RESTRAINING ORDERS</li><li>PROBATE</li><li>TITLES</li><li>SHARIAH LAW</li>
  </ul>
</header>

<section class="hero abs" role="img" aria-label="Photo of a family with a young daughter meeting a legal advisor at a table"></section>
<h1 class="hero-title abs">GET YOUR LEGAL ADVICE<br><span class="red">AND PROTECT YOU<br>AND YOUR BUSINESS</span></h1>
<p class="hero-text abs">Vivamus porttitor purus nisi eleifend libero a tempus libero lectus feugiat felis Morbi diam mauris</p>
<div class="btn btn-yellow" style="left:190px;top:411px;width:135px;height:43px">READ MORE</div>
<div class="slider-dots abs" style="left:566px;top:564px"><span class="ring"></span><span></span><span></span><span></span></div>

<h2 class="section-title services-title abs">OUR SERVICES</h2>
<svg class="arrow" style="left:126px" width="24" height="52" viewBox="0 0 24 52"><path d="M22 2 2 26l20 24" fill="none" stroke="#888" stroke-width="2"/></svg>
<svg class="arrow" style="left:1034px" width="24" height="52" viewBox="0 0 24 52"><path d="M2 2l20 24L2 50" fill="none" stroke="#888" stroke-width="2"/></svg>

<div class="service" style="left:182px">
  <svg width="84" height="84" viewBox="0 0 84 84"><circle cx="42" cy="42" r="39" fill="none" stroke="var(--yellow)" stroke-width="4"/><g fill="none" stroke="var(--red)" stroke-width="2.5"><circle cx="31" cy="33" r="7"/><circle cx="53" cy="33" r="7"/><circle cx="42" cy="47" r="5"/><path d="M20 60c0-9 5-14 11-14M64 60c0-9-5-14-11-14M34 64c0-6 4-9 8-9s8 3 8 9"/></g></svg>
  <h3>FAMILY LAW</h3>
  <p>Vivamus porttitor purus nisi eleifend libero a tempus libero lectus feugiat felis Morbi diam mauris viverra in gravida</p>
  <div class="more">READ MORE</div>
</div>
<div class="service" style="left:403px">
  <svg width="84" height="84" viewBox="0 0 84 84"><circle cx="42" cy="42" r="39" fill="none" stroke="var(--yellow)" stroke-width="4"/><g fill="none" stroke="var(--red)" stroke-width="2.5"><rect x="22" y="28" width="36" height="28" rx="3"/><path d="M30 28v-6h20v6"/><circle cx="50" cy="52" r="9" fill="#fff"/><path d="M50 47v10M47 50h5"/></g></svg>
  <h3>DEBT RECOVERY</h3>
  <p>Vivamus porttitor purus nisi eleifend libero a tempus libero lectus feugiat felis Morbi diam mauris viverra in gravida</p>
  <div class="more">READ MORE</div>
</div>
<div class="service" style="left:624px;top:734px">
  <svg width="84" height="84" viewBox="0 0 84 84"><circle cx="42" cy="42" r="39" fill="none" stroke="var(--yellow)" stroke-width="4"/><g fill="none" stroke="var(--red)" stroke-width="2.5"><rect x="26" y="22" width="26" height="38" rx="2"/><path d="M31 32h16M31 39h16M31 46h10"/><path d="M57 24v32l3 5 3-5V24z"/></g></svg>
  <h3>LEASES</h3>
  <p>Vivamus porttitor purus nisi eleifend libero a tempus libero lectus feugiat felis Morbi diam mauris viverra in gravida</p>
  <div class="more">READ MORE</div>
</div>
<div class="service" style="left:844px;top:734px">
  <svg width="84" height="84" viewBox="0 0 84 84"><circle cx="42" cy="42" r="39" fill="none" stroke="var(--yellow)" stroke-width="4"/><g fill="none" stroke="var(--red)" stroke-width="2.5"><rect x="32" y="20" width="20" height="42" rx="4"/><circle cx="42" cy="29" r="4"/><circle cx="42" cy="41" r="4"/><circle cx="42" cy="53" r="4"/><path d="M32 28h-5M32 40h-5M52 28h5M52 40h5"/></g></svg>
  <h3>CRIMES &amp;<br>TRAFFIC, WILLS</h3>
  <p>Vivamus porttitor purus nisi eleifend libero a tempus libero lectus feugiat felis Morbi</p>
  <div class="more">READ MORE</div>
</div>

<div class="about-photo abs" role="img" aria-label="Photo of three colleagues reviewing documents at an office desk"></div>
<div class="about-panel abs"></div>
<div class="eyebrow abs">LEXMORA LEGAL</div>
<h2 class="section-title about-title abs">ABOUT US</h2>
<p class="about-text abs">Vivamus porttitor purus nisi eleifend libero a tempus libero lectus feugiat felis Morbi diam mauris viverra in gravida eu mattis in ante Morbi eget arcu Morbi porta libero id ullamcorper nonummy nibh ligula pulvinar metus eget consectetuer augue nisi quis lacus Ut ac mi quis lacus mollis aliquam</p>
<div class="btn btn-red" style="left:675px;top:1398px;width:133px;height:42px">READ MORE</div>

<section class="testimonial abs" role="img" aria-label="Faded black and white photo of an office meeting"></section>
<h2 class="section-title client-title abs">WHAT OUR CLIENT SAYS</h2>
<div class="avatar abs" role="img" aria-label="Portrait photo of a smiling client"></div>
<svg class="quote-mark abs" width="50" height="50" viewBox="0 0 50 50"><circle cx="25" cy="25" r="25" fill="var(--red)"/><path d="M16 31c0-6 2-10 6-12l1 2c-2 1-3 3-3 5h3v5zM27 31c0-6 2-10 6-12l1 2c-2 1-3 3-3 5h3v5z" fill="#fff"/></svg>
<p class="quote abs">Morbi diam mauris viverra in gravida eu mattis in ante Morbi eget arcu Morbi porta libero id ullamcorper nonummy nibh ligula pulvi-nar metus eget consectetuer augue nisi quis lacus</p>
<div class="author abs">BY AUTHOR NAME</div>
<div class="slider-dots abs" style="left:455px;top:1829px;gap:5px"><span style="width:8px;height:8px;background:#222"></span><span style="width:8px;height:8px;background:#222"></span><span style="width:8px;height:8px;background:#4aa"></span><span style="width:8px;height:8px;background:#222"></span><span style="width:8px;height:8px;background:#222"></span></div>

<div class="why-panel abs"></div>
<div class="why-photo abs" role="img" aria-label="Photo of a senior couple signing papers with an advisor"></div>
<h2 class="section-title why-title abs">WHY CHOOSE US</h2>
<p class="why-text abs">Vivamus porttitor purus nisi eleifend libero a tempus libero lectus feugiat felis Morbi diam mauris viverra in gravida eu mattis in ante Morbi eget arcu Morbi porta libero id ullamcorper nonummy nibh ligula pulvinar metus eget consectetuer augue nisi quis lacus Ut ac mi quis lacus mollis aliquam vscelerisque mi</p>
<div class="btn btn-yellow" style="left:184px;top:2259px;width:135px;height:43px">READ MORE</div>

<h2 class="section-title people-title abs">OUR PEOPLE</h2>
<p class="people-text abs">Vivamus porttitor purus nisi eleifend libero a tempus libero lectus feugiat felis Morbi diam mauris viverra in gravida eu mattis in ante Morbi eget arcu&nbsp; Morbi porta libero id ullamcorper nonummy nibh ligula pulvinar metus eget consectetuer augue nisi quis lacus Ut ac mi quis lacus mollis aliquam</p>
<div class="member" style="left:188px"><div class="photo" role="img" aria-label="Portrait photo of a team member"></div><h4>Member Name</h4><span>City Location</span></div>
<div class="member" style="left:405px"><div class="photo" role="img" aria-label="Portrait photo of a team member"></div><h4>Member Name</h4><span>City Location</span></div>
<div class="member" style="left:619px"><div class="photo" role="img" aria-label="Portrait photo of a team member"></div><h4>Member Name</h4><span>City Location</span></div>
<div class="member" style="left:836px"><div class="photo" role="img" aria-label="Portrait photo of a team member"></div><h4>Member Name</h4><span>City Location</span></div>

<footer class="site-footer abs"></footer>
<nav class="footer-nav abs"><span>HOME</span><span>ABOUT US</span><span>OUR PEOPLE</span><span>SERVICES</span><span>CONTACT US</span></nav>
<div class="copyright abs">© 2018 Company Name&nbsp; All right reserved</div>
<div class="socials abs" aria-label="Social links"><span></span><span></span><span></span><span></span></div>

</body>
</html>
```